Sickle Cell Patient Flyer

I need this be appealing to families dealing with sickle cell disease. Both informative-introducing the idea that a stroke prevention program is not only easy for their children but necessary. Stroke is a risk to all with children with SCD.
I included a few info flyers from the Brainward Alliance and licensed to me photos I like. I am open to suggestions.
web address is carebrightpath.example
Call to schedule 855-555-0148
TCD is a safe and accurate tool that makes stroke prevention possible for your SCD patients and family.
Risk is highest for SCD sufferers age 2 to 5. Protect your childs future.

Target Market(s)

Parents, families and medical professionals

Industry/Entity Type

Medical wellness

Font styles to use
Other font styles liked:
• something close to my logo font

Colors
0094D4
00A9DD
6FCCEA
C7EBF8
E9F6FB

Requirements
Nice to have
• pictures of kids (Children of color) pictures of Brains, kids happy with medical professionals
Should not have
• dark colors

```html
<!DOCTYPE html>
<html lang="en">
<head>
<meta charset="utf-8">
<title>CareBright Path – Stroke Prevention Flyer</title>
<link href="https://fonts.googleapis.com/css2?family=Poppins:wght@400;500;600;700;800&family=Mystery+Quest&display=swap" rel="stylesheet">
<style>
  :root {
    --page-bg: #e9eef3;
    --paper: #ffffff;
    --ink: #2a2f36;
    --brand-blue: #2f8fd8;
    --bright-blue: #0094d4;
    --deep-blue: #0b4a8b;
    --mint: #6fcf9f;
    --call-blue: #4aa0dc;
    --sky: #c7ebf8;
    --ice: #e9f6fb;
    --divider: #e3e7eb;
  }
  * { box-sizing: border-box; margin: 0; padding: 0; }
  html, body { width: 1200px; height: 2400px; overflow: hidden; background: var(--page-bg); }
  body { font-family: "Poppins", sans-serif; color: var(--ink); position: relative; }

  .flyer {
    position: absolute; left: 40px; top: 475px;
    width: 1120px; height: 1450px;
    background: var(--paper);
    overflow: hidden;
    box-shadow: 0 6px 24px rgba(30, 50, 80, 0.12);
  }

  .hero-photo {
    position: absolute; left: 480px; top: 43px; width: 640px; height: 509px;
    z-index: 0;
    background: radial-gradient(ellipse at 55% 60%, #f2c53a 0 22%, #cfeee0 40%, #e6f3fb 62%, #ffffff 80%);
  }

  .brand {
    position: absolute; left: 52px; top: 128px; z-index: 2;
    display: flex; align-items: center; gap: 14px;
    white-space: nowrap;
  }
  .brand-mark { width: 40px; height: 40px; background: var(--brand-blue); flex: none; }
  .brand-name { font-weight: 700; font-size: 40px; color: var(--brand-blue); line-height: 1; }

  .headline { position: absolute; left: 52px; top: 322px; z-index: 2; }
  .headline-lead { font-size: 42px; font-weight: 400; line-height: 1.0; color: var(--ink); }
  .headline-key { font-size: 56px; font-weight: 700; line-height: 1.0; color: var(--brand-blue); margin-top: 6px; }

  .protect-band {
    position: absolute; left: 52px; top: 552px; width: 1006px; height: 174px; z-index: 2;
    background: var(--deep-blue); border-radius: 22px;
    display: flex; align-items: center;
  }
  .protect-title {
    width: 538px; padding-left: 34px;
    font-family: "Mystery Quest", cursive; font-size: 60px; line-height: 0.95; font-weight: 400;
  }
  .protect-title .line-white { color: #ffffff; display: block; }
  .protect-title .line-mint { color: var(--mint); display: block; }
  .protect-divider { width: 0; height: 120px; border-left: 2px dashed rgba(255,255,255,0.5); }
  .protect-copy {
    padding-left: 36px; width: 440px;
    color: #ffffff; font-size: 27px; font-weight: 500; line-height: 1.15;
  }

  .facts { position: absolute; left: 0; top: 770px; width: 1120px; height: 250px; }
  .fact { position: absolute; top: 0; text-align: center; }
  .fact svg { display: block; margin: 0 auto 18px; }
  .fact p { font-size: 21px; font-weight: 500; line-height: 1.18; color: var(--ink); }
  .fact-1 { left: 60px; width: 260px; }
  .fact-2 { left: 380px; width: 290px; }
  .fact-3 { left: 720px; width: 340px; }
  .fact-rule { position: absolute; top: 0; width: 2px; height: 245px; background: var(--divider); }

  .care-photo {
    position: absolute; left: 0; top: 1044px; width: 573px; height: 406px;
    background: linear-gradient(115deg, #e7c8b2 0%, #d9a86f 28%, #f2f2f2 55%, #ffffff 100%);
  }

  .screening { position: absolute; left: 588px; top: 1100px; width: 480px; z-index: 2; }
  .screening-lead { font-size: 29px; font-weight: 700; color: var(--deep-blue); line-height: 1.1; }
  .screening-copy { font-size: 23px; font-weight: 500; line-height: 1.18; color: var(--ink); }

  .call-bar {
    position: absolute; left: 523px; top: 1230px; width: 507px; height: 56px; z-index: 2;
    background: var(--call-blue);
    font-family: "Mystery Quest", cursive; font-size: 46px; color: #ffffff;
    line-height: 56px; padding-left: 64px; white-space: nowrap;
  }

  .contact { position: absolute; left: 588px; top: 1298px; z-index: 2; }
  .contact-row { display: flex; align-items: center; gap: 14px; }
  .contact-phone { font-size: 48px; font-weight: 700; color: var(--ink); letter-spacing: 1px; }
  .contact-web { font-size: 27px; font-weight: 600; color: var(--ink); margin-top: 4px; }
  .contact-icon { flex: none; }
</style>
</head>
<body>
  <main class="flyer">
    <div class="hero-photo" role="img" aria-label="Smiling child in a yellow sweater raising both fists, in front of outlined brain drawings in green and blue"></div>

    <div class="brand">
      <span class="brand-mark"></span>
      <span class="brand-name">CareBright Path</span>
    </div>

    <div class="headline">
      <p class="headline-lead">Stroke Prevention<br>for Children</p>
      <p class="headline-key">with sickle cell<br>disease is possible!</p>
    </div>

    <section class="protect-band">
      <h2 class="protect-title">
        <span class="line-white">PROTECT YOUR</span>
        <span class="line-mint">CHILDS FUTURE</span>
      </h2>
      <span class="protect-divider"></span>
      <p class="protect-copy">TCD is a safe and accurate tool that makes stroke prevention possible for your SCD patients and family.</p>
    </section>

    <section class="facts">
      <div class="fact fact-1">
        <svg width="120" height="110" viewBox="0 0 120 110" fill="none" stroke-width="3" stroke-linecap="round" stroke-linejoin="round">
          <rect x="52" y="8" width="58" height="90" rx="4" stroke="#0b4a8b"/>
          <rect x="68" y="3" width="26" height="10" rx="2" stroke="#0b4a8b"/>
          <path d="M92 28v14M85 35h14" stroke="#0b4a8b"/>
          <path d="M62 55h38M62 65h38M62 75h30" stroke="#0b4a8b"/>
          <path d="M10 20v30a16 16 0 0 0 32 0V20" stroke="#6fcf9f"/>
          <path d="M26 66v20a12 12 0 0 0 24 0v-20" stroke="#6fcf9f"/>
          <circle cx="50" cy="60" r="6" stroke="#6fcf9f"/>
        </svg>
        <p>Simple and<br>painless screening<br>for your child.</p>
      </div>
      <span class="fact-rule" style="left:351px"></span>
      <div class="fact fact-2">
        <svg width="140" height="112" viewBox="0 0 140 112" fill="none" stroke="#0b4a8b" stroke-width="3" stroke-linecap="round" stroke-linejoin="round">
          <rect x="4" y="14" width="96" height="64" rx="4"/>
          <rect x="14" y="24" width="76" height="44" rx="2"/>
          <path d="M32 50a20 14 0 0 1 40 0z"/>
          <rect x="4" y="86" width="96" height="20" rx="3"/>
          <path d="M16 96h10M32 96h10M48 96h10M66 92h22v8H66z"/>
          <path d="M100 96h12a6 6 0 0 0 6-6V40"/>
          <rect x="110" y="14" width="16" height="26" rx="4"/>
          <path d="M128 6a14 14 0 0 1 6 12"/>
        </svg>
        <p>Our Screening uses<br>ultrasound which is<br>transcranial doppler</p>
      </div>
      <span class="fact-rule" style="left:695px"></span>
      <div class="fact fact-3">
        <svg width="120" height="112" viewBox="0 0 120 112" fill="none" stroke-width="3" stroke-linecap="round" stroke-linejoin="round">
          <path d="M60 4l-6 16h10l-6 14" stroke="#6fcf9f"/>
          <path d="M20 22l12 10-4 6 12 6" stroke="#6fcf9f"/>
          <path d="M100 22l-12 10 4 6-12 6" stroke="#6fcf9f"/>
          <ellipse cx="60" cy="74" rx="40" ry="28" stroke="#0b4a8b"/>
          <path d="M60 48v52M40 64c6 4 10 4 14 0M66 64c6 4 10 4 14 0M38 84c8-4 14-2 18 2M64 86c6-4 12-4 18 0" stroke="#0b4a8b"/>
        </svg>
        <p>About 11% of SCD<br>patients have strokes before<br>age 20 with the highest risk<br>between age 2 and 5.</p>
      </div>
    </section>

    <div class="care-photo" role="img" aria-label="Young girl holding a teddy bear and a stethoscope, smiling with a doctor in a white coat"></div>

    <section class="screening">
      <p class="screening-lead">Screening or early signs</p>
      <p class="screening-copy">of stroke can be a tool to for early diagnosis allowing for treatments that eliminate the risk.</p>
    </section>

    <div class="call-bar">CALL TO SCHEDULE</div>

    <div class="contact">
      <div class="contact-row">
        <svg class="contact-icon" width="34" height="34" viewBox="0 0 34 34">
          <circle cx="17" cy="17" r="17" fill="#0b4a8b"/>
          <path d="M11 9c1-1 2-1 3 0l2 3c.5 1 .3 1.8-.4 2.4l-1.2 1c.9 2 2.3 3.4 4.2 4.2l1-1.2c.6-.7 1.4-.9 2.4-.4l3 2c1 1 1 2 0 3l-1.4 1.4c-1.6 1.6-5.4.6-9-3s-4.6-7.4-3-9z" fill="#ffffff"/>
        </svg>
        <span class="contact-phone">855-555-0148</span>
      </div>
      <div class="contact-row">
        <svg class="contact-icon" width="34" height="34" viewBox="0 0 34 34" fill="none">
          <circle cx="17" cy="17" r="17" fill="#0b4a8b"/>
          <circle cx="17" cy="17" r="9" stroke="#ffffff" stroke-width="2"/>
          <path d="M8 17h18M17 8c-4 5-4 13 0 18M17 8c4 5 4 13 0 18" stroke="#ffffff" stroke-width="2"/>
        </svg>
        <span class="contact-web">www.carebrightpath.example</span>
      </div>
    </div>
  </main>
</body>
</html>
```